Kestrel Wiring - Electrician company flyers for new clients

I want a flyer that will be dropped into mailboxes and will hopefully stand out more that the ones i have tried to mock up. I have attached my latest design to give you an idea but it is rather boring.

The aim is obviously to entice new customers into calling me for any electrical work, mainly domestic but i also do commercial work.
I will also upload a photo of my business card so that it can be used as a reference and my website is www.kestrelwiring.co.nz for any extra information.

Ideally the flyer will be DL size
measurements from printmorrow is that's any help
Document Trim Size
99 x 210 mm
1169 x 2480 pixels
Full Bleed Size
102 x 213 mm
1205 x 2516 pixels

Target Market(s)

Domestic electrical works

Industry/Entity Type

Electrician

Requirements
Must have
• all of my contact details -
• Dean Forsyth
• Dean@kestrelwiring.co.nz
• 027 3815 942
• www.kestrelwiring.co.nz
• A little write up similar to the one written on my draft but there's probably alot of room for improvement as my writing skills are lacking.
Nice to have
• clear and concise writing so that people wont throw it away before reading

```html
<!DOCTYPE html>
<html lang="en">
<head>
<meta charset="utf-8">
<title>Kestrel Wiring – DL Flyer</title>
<link rel="stylesheet" href="https://fonts.googleapis.com/css2?family=Open+Sans:wght@400;600;700;800&family=Oswald:wght@600&family=Archivo+Black&display=swap">
<style>
  :root {
    --brand-blue: #0a9be0;
    --panel-blue: #0794db;
    --steel-grey: #6e6f71;
    --ink: #1b1b1b;
    --white: #ffffff;
    --page-bg: #5b5b5b;
  }
  * { margin: 0; padding: 0; box-sizing: border-box; }
  html, body {
    width: 1200px; height: 1200px; overflow: hidden;
    background: var(--page-bg);
  }
  .flyer {
    position: absolute; left: 373px; top: 126px;
    width: 454px; height: 947px;
    background: var(--white);
    overflow: hidden;
    font-family: "Open Sans", sans-serif;
  }
  .header-backdrop {
    position: absolute; left: 0; top: 0; width: 454px; height: 230px;
    background: linear-gradient(180deg, #f4f6f8 0%, #e6eaee 55%, #dfe4e8 100%);
  }
  .service-photo {
    position: absolute; left: 0; top: 583px; width: 454px; height: 270px;
    background: linear-gradient(120deg, #e9eef2 0%, #c9d3dc 28%, #b8342f 40%, #27457a 58%, #1f3a6b 72%, #f2a21c 86%, #eef1f4 100%);
  }
  .flyer-shapes { position: absolute; left: 0; top: 0; }
  .brand-name {
    position: absolute; left: 0; top: 50px; width: 454px;
    text-align: center;
    font-family: "Open Sans", sans-serif; font-weight: 800;
    color: var(--brand-blue);
    font-size: 52px; line-height: 58px; letter-spacing: 2px;
    text-transform: uppercase;
  }
  .headline {
    position: absolute; left: 22px; top: 240px; width: 420px;
    color: var(--white);
  }
  .headline-main {
    display: block;
    font-family: "Oswald", sans-serif; font-weight: 600;
    font-size: 49px; line-height: 52px; letter-spacing: -0.5px;
    text-transform: uppercase; white-space: nowrap;
  }
  .headline-sub {
    display: block; margin-top: 2px;
    font-family: "Archivo Black", sans-serif;
    font-size: 24.5px; line-height: 28px; letter-spacing: 0.6px;
    text-transform: uppercase; white-space: nowrap;
  }
  .headline-rule {
    position: absolute; left: 22px; top: 334px;
    width: 129px; height: 3px; background: var(--white);
  }
  .intro {
    position: absolute; left: 22px; top: 347px; width: 409px;
    color: var(--white);
    font-size: 20.2px; line-height: 24.4px;
    text-align: justify;
  }
  .locality {
    position: absolute; left: 22px; top: 510px; width: 409px;
    color: var(--white);
    font-size: 14.6px; line-height: 19px; font-weight: 600;
    text-align: justify;
  }
  .contact-title {
    position: absolute; left: 0; top: 838px; width: 454px;
    text-align: center;
    color: var(--brand-blue);
    font-weight: 800; font-size: 21px; letter-spacing: 0.8px;
  }
  .contact-rule {
    position: absolute; left: 175px; top: 866px;
    width: 102px; height: 2px; background: var(--steel-grey);
  }
  .contact-name {
    position: absolute; left: 22px; top: 876px;
    color: var(--brand-blue); font-weight: 600; font-size: 19px;
  }
  .contact-line {
    position: absolute; display: flex; align-items: center; gap: 5px;
    color: var(--ink); white-space: nowrap;
  }
  .contact-line svg { flex: none; }
  .contact-phone { left: 239px; top: 876px; font-weight: 700; font-size: 19px; }
  .contact-email { left: 22px; top: 909px; font-size: 13.8px; }
  .contact-web { left: 239px; top: 909px; font-size: 13.8px; }
</style>
</head>
<body>
  <main class="flyer">
    <div class="header-backdrop" role="img" aria-label="Faded photo of a harbour city skyline"></div>
    <div class="service-photo" role="img" aria-label="Photo of an electrician in a hard hat testing wiring in a switchboard"></div>

    <svg class="flyer-shapes" width="454" height="947" viewBox="0 0 454 947" aria-hidden="true">
      <polygon fill="var(--steel-grey)" points="0,182 227,216 454,182 454,193 227,227 0,193"/>
      <polygon fill="var(--panel-blue)" points="0,192 227,226 454,192 454,583 0,583"/>
      <polygon fill="var(--steel-grey)" points="0,838 227,804 454,838 454,849 227,815 0,849"/>
      <polygon fill="var(--white)" points="0,848 227,814 454,848 454,947 0,947"/>
    </svg>

    <h1 class="brand-name">Kestrel<br>Wiring</h1>

    <h2 class="headline">
      <span class="headline-main">Do you need a local</span>
      <span class="headline-sub">&amp; reliable electrician?</span>
    </h2>
    <div class="headline-rule"></div>

    <p class="intro">Specializing in residential and commercial electrical services, we are dedicated to providing customer service that is second to none. Whether you need a small wiring fix or the full installation , we can get the job done right.</p>

    <p class="locality">Based in Kowhai Cove, We are your local Electricians with our main aim to keep our work and communication to a very high standard.</p>

    <h3 class="contact-title">CONTACT US TODAY</h3>
    <div class="contact-rule"></div>

    <p class="contact-name">Dean Forsyth</p>

    <p class="contact-line contact-phone">
      <svg width="16" height="16" viewBox="0 0 24 24"><path fill="var(--brand-blue)" d="M6.6 10.8a15.1 15.1 0 0 0 6.6 6.6l2.2-2.2a1 1 0 0 1 1-.25 11.4 11.4 0 0 0 3.6.57 1 1 0 0 1 1 1V20a1 1 0 0 1-1 1A17 17 0 0 1 3 4a1 1 0 0 1 1-1h3.5a1 1 0 0 1 1 1c0 1.25.2 2.45.57 3.57a1 1 0 0 1-.25 1z"/></svg>
      027 3815 942
    </p>

    <p class="contact-line contact-email">
      <svg width="14" height="11" viewBox="0 0 14 11"><rect x="0.5" y="1" width="13" height="9" fill="var(--brand-blue)"/><path d="M1 1.5l6 4.5 6-4.5" fill="none" stroke="#fff" stroke-width="1.2"/></svg>
      Dean@kestrelwiring.co.nz
    </p>

    <p class="contact-line contact-web">
      <svg width="16" height="16" viewBox="0 0 16 16"><g fill="none" stroke="var(--brand-blue)" stroke-width="1.3"><circle cx="8" cy="8" r="6.8"/><ellipse cx="8" cy="8" rx="3" ry="6.8"/><path d="M1.2 8h13.6M2.3 4.6h11.4M2.3 11.4h11.4"/></g></svg>
      www.kestrelwiring.co.nz
    </p>
  </main>
</body>
</html>
```